company name - HARLOWMERE AIRPORT TRANSFER.
include this information please .....25 YEARS EXPERIENCE / CARS+MPVS+MINIBUSES AVAILABLE - ALL AT SAME PRICE AT ANY TIME OF DAY. NO EXTRA HIDDEN CHARGES.

PRICES [ selection ] ......

BRAXMOOR ....£100
CORVALE ....£130
DERRIN...£55.00
QUILLBOURNE ...£60.00
HALVERSTOKE ...£100.00
UPPER KESTLING ...£100,00
QUAYSIDE AIRPORT ...£95.00

```html
<!DOCTYPE html>
<html lang="en">
<head>
<meta charset="utf-8">
<title>Harlowmere Airport Transfer – Price Flyer</title>
<link href="https://fonts.googleapis.com/css2?family=Lato:ital,wght@0,400;0,700;0,900;1,900&family=Oswald:wght@500;700&display=swap" rel="stylesheet">
<style>
  :root {
    --red: #e3131c;
    --red-dark: #b90d14;
    --red-light: #f0373d;
    --black: #111111;
    --white: #ffffff;
    --paper: #f4f4f4;
    --grey: #cfcfcf;
    --page: #e6e6e6;
  }
  * { margin: 0; padding: 0; box-sizing: border-box; }
  html, body { width: 1200px; height: 995px; overflow: hidden; }
  body { background: var(--page); font-family: "Lato", Arial, sans-serif; position: relative; }

  .flyer {
    position: absolute; left: 36px; top: 97px;
    width: 1128px; height: 801px; overflow: hidden;
    box-shadow: 0 4px 18px rgba(0,0,0,.18);
  }
  .flyer-shapes { position: absolute; inset: 0; width: 100%; height: 100%; }

  .brand-mark {
    position: absolute; left: 33px; top: 57px; width: 132px; height: 132px;
    border-radius: 50%; background: var(--red);
    border: 6px solid var(--grey);
  }
  .brand-name {
    position: absolute; left: 192px; top: 88px; width: 390px;
    font: 700 26px/1 "Lato", Arial, sans-serif; color: var(--black);
    white-space: nowrap;
  }
  .brand-rule { position: absolute; left: 192px; top: 124px; width: 380px; height: 3px; background: var(--black); }
  .experience {
    position: absolute; left: 192px; top: 132px;
    font: 700 43px/1 "Oswald", Impact, sans-serif; color: var(--black); white-space: nowrap;
  }
  .experience .accent { color: var(--red); }

  .hours-badge {
    position: absolute; left: 609px; top: 57px; width: 70px; height: 70px;
    border-radius: 50%; background: var(--white); border: 3px solid var(--black);
    display: flex; flex-direction: column; align-items: center; justify-content: center;
    line-height: 1;
  }
  .hours-badge .num { font: 700 25px/1 "Oswald", sans-serif; color: var(--red); }
  .hours-badge .unit { font: 700 13px/1 "Lato", sans-serif; color: var(--black); }

  .price-list { position: absolute; left: 44px; top: 255px; width: 522px; list-style: none; }
  .price-row { height: 42.5px; display: flex; align-items: center; color: var(--white); }
  .price-row .dot { width: 13px; height: 13px; border-radius: 50%; background: var(--black); margin-right: 24px; flex: none; }
  .price-row .place { font: 700 24px/1 "Lato", sans-serif; letter-spacing: .5px; white-space: nowrap; }
  .price-row .leader { flex: 1; height: 2px; background: var(--black); margin: 0 18px 0 16px; }
  .price-row .price { font: 500 28px/1 "Oswald", sans-serif; width: 58px; }

  .fleet {
    position: absolute; left: 40px; top: 610px;
    font: italic 900 28px/1 "Lato", sans-serif; color: var(--black); white-space: nowrap;
  }
  .fleet .bullet { color: var(--red); }
  .fleet .accent { color: var(--red); }
  .fleet-note {
    position: absolute; left: 115px; top: 650px;
    font: 700 20px/1 "Lato", sans-serif; color: var(--black); white-space: nowrap;
  }
  .call {
    position: absolute; left: 40px; top: 712px;
    font: 700 37px/1 "Oswald", Impact, sans-serif; color: var(--white); white-space: nowrap; letter-spacing: .5px;
  }
  .call .number { color: var(--black); margin-left: 6px; }

  .charges-badge {
    position: absolute; left: 676px; top: 579px; width: 174px; height: 174px;
    border-radius: 50%; background: var(--red);
    border: 8px solid var(--grey); box-shadow: 0 0 0 3px var(--white) inset;
    display: flex; flex-direction: column; align-items: center; justify-content: center;
    color: var(--white); text-align: center; line-height: 1.05;
  }
  .charges-badge .small { font: 700 19px "Lato", sans-serif; }
  .charges-badge .big { font: 700 32px "Lato", sans-serif; margin: 4px 0; }
</style>
</head>
<body>
  <section class="flyer">
    <svg class="flyer-shapes" viewBox="0 0 806 572" preserveAspectRatio="none">
      <defs>
        <linearGradient id="headerFill" x1="0" y1="0" x2="0" y2="1">
          <stop offset="0" stop-color="#ffffff"/>
          <stop offset="1" stop-color="#e2e2e2"/>
        </linearGradient>
        <linearGradient id="redFill" x1="0" y1="0" x2="1" y2="1">
          <stop offset="0" stop-color="#c50f16"/>
          <stop offset=".5" stop-color="#ef2a30"/>
          <stop offset="1" stop-color="#c50f16"/>
        </linearGradient>
        <linearGradient id="photoFill" x1="0" y1="0" x2="0" y2="1">
          <stop offset="0" stop-color="#cfe0ee"/>
          <stop offset=".35" stop-color="#eef3f6"/>
          <stop offset=".45" stop-color="#d83a3a"/>
          <stop offset=".8" stop-color="#b8171c"/>
          <stop offset=".85" stop-color="#5c5c5c"/>
          <stop offset="1" stop-color="#9a9a9a"/>
        </linearGradient>
      </defs>
      <rect class="band-top" x="0" y="0" width="806" height="13" fill="var(--red)"/>
      <rect class="header" x="0" y="13" width="806" height="149" fill="url(#headerFill)"/>
      <rect x="0" y="160" width="806" height="3" fill="var(--black)"/>
      <rect class="price-panel" x="0" y="163" width="806" height="248" fill="url(#redFill)"/>
      <rect x="0" y="410" width="806" height="3" fill="var(--black)"/>
      <rect class="info-band" x="0" y="413" width="806" height="77" fill="url(#headerFill)"/>
      <rect x="0" y="489" width="806" height="3" fill="var(--black)"/>
      <rect class="call-band" x="0" y="492" width="806" height="61" fill="url(#redFill)"/>
      <rect x="0" y="553" width="806" height="3" fill="var(--black)"/>
      <rect class="band-bottom" x="0" y="556" width="806" height="16" fill="var(--white)"/>
      <path transform="translate(-28 0)" fill="var(--red)"
            d="M612 0 C520 110 455 300 490 430 C510 500 545 545 578 572 L806 572 L806 0 Z"/>
      <path transform="translate(-12 0)" fill="var(--black)"
            d="M612 0 C520 110 455 300 490 430 C510 500 545 545 578 572 L806 572 L806 0 Z"/>
      <path class="fleet-photo" role="img" aria-label="Photo of a row of red minibuses parked outside a depot under a blue sky"
            fill="url(#photoFill)"
            d="M612 0 C520 110 455 300 490 430 C510 500 545 545 578 572 L806 572 L806 0 Z"/>
    </svg>

    <div class="brand-mark"></div>
    <div class="brand-name">Harlowmere Airport Transfer</div>
    <div class="brand-rule"></div>
    <div class="experience"><span class="accent">25 YEARS</span> EXPERIENCE</div>
    <div class="hours-badge"><span class="num">24</span><span class="unit">HRS</span></div>

    <ul class="price-list">
      <li class="price-row"><span class="dot"></span><span class="place">BRAXMOOR</span><span class="leader"></span><span class="price">£100</span></li>
      <li class="price-row"><span class="dot"></span><span class="place">CORVALE</span><span class="leader"></span><span class="price">£130</span></li>
      <li class="price-row"><span class="dot"></span><span class="place">DERRIN</span><span class="leader"></span><span class="price">£55</span></li>
      <li class="price-row"><span class="dot"></span><span class="place">QUILLBOURNE</span><span class="leader"></span><span class="price">£60</span></li>
      <li class="price-row"><span class="dot"></span><span class="place">HALVERSTOKE</span><span class="leader"></span><span class="price">£100</span></li>
      <li class="price-row"><span class="dot"></span><span class="place">UPPER KESTLING</span><span class="leader"></span><span class="price">£100</span></li>
      <li class="price-row"><span class="dot"></span><span class="place">QUAYSIDE AIRPORT</span><span class="leader"></span><span class="price">£95</span></li>
    </ul>

    <div class="fleet"><span class="bullet">•</span> CARS <span class="bullet">•</span> MPVS <span class="bullet">•</span> MINIBUSES <span class="accent">AVAILABLE</span></div>
    <div class="fleet-note">ALL AT SAME PRICE AT ANY TIME OF DAY</div>
    <div class="call">CALL US <span class="number">020 7946 0321</span></div>

    <div class="charges-badge">
      <span class="small">NO EXTRA</span>
      <span class="big">HIDDEN</span>
      <span class="small">CHARGES</span>
    </div>
  </section>
</body>
</html>
```